依頼詳細
タイトル+20~30行のテキストが主。
テキストをお読みいただき雰囲気に合ったデザインをお願いします。
イメージ
重厚感、誠実、まじめ。
もし動画にするならBGMはカゼノワの「白い石の坂道」のイメージ。
曇り空に一筋の光
とか
全面的に黒い雰囲気の中に一滴の赤

或いは画像の中の青空を活かしても面白いかもしれません。
記載項目
・添付のテキスト
・背景に使う写真は添付ファイルを使ってもいいし、使わなくても構いません
・最後の「松浦産業株式会社」は検索ウィンドウとし、右側に「検索」ボタンをつけてください。
・チラシ最下段に「説明会情報は弊社HPでご確認ください」
サイズ
A4
ページ数
片面
希望イメージ
シンプル 複雑
単色 カラフル
暗い 明るい
日常 高級
遊び心 厳粛
未来的 伝統的
女性的 男性的
希望する色
水色系、グレー系
納品ファイル
• フォトショップ形式 (.psd)
補足説明
追加でお願いするポスターは約72cm×22cmで一般的なサイズ
合同企業説明会のときにブースを通る学生さんの足を止めるためのインパクト大なポスターを希望します。

希望通りのイメージで仕上げて頂きました。
ありがとうございます。

多数のご提案頂きありがとうございました。

```html
<!DOCTYPE html>
<html lang="ja">
<head>
<meta charset="utf-8">
<title>松浦産業株式会社 採用ポスター</title>
<link rel="stylesheet" href="https://fonts.googleapis.com/css2?family=Noto+Sans+JP:wght@400;500;700&display=swap">
<style>
  :root {
    --sky-top: #4f6275;
    --sky-mid: #8fa3b5;
    --sky-light: #c3d0da;
    --sky-bottom: #6f7f8c;
    --ink-light: #ffffff;
    --accent-red: #d8202a;
    --field-bg: #ffffff;
    --field-ink: #222222;
    --button-bg: #8a939b;
  }
  * { margin: 0; padding: 0; box-sizing: border-box; }
  html, body { width: 849px; height: 1200px; overflow: hidden; }
  body { font-family: "Noto Sans JP", sans-serif; }
  .poster {
    position: relative;
    width: 849px;
    height: 1200px;
    overflow: hidden;
    color: var(--ink-light);
  }
  .sky-photo {
    position: absolute;
    inset: 0;
    background:
      radial-gradient(ellipse 60% 30% at 70% 45%, rgba(230,238,244,.65), transparent 70%),
      linear-gradient(180deg, var(--sky-top) 0%, var(--sky-mid) 35%, var(--sky-light) 55%, var(--sky-mid) 75%, var(--sky-bottom) 100%);
  }
  .headline {
    position: absolute;
    left: 10px;
    top: 8px;
    font-weight: 500;
    font-size: 86px;
    line-height: 106px;
    letter-spacing: 0;
    white-space: nowrap;
    text-shadow: 0 2px 6px rgba(0,0,0,.25);
  }
  .manifesto {
    position: absolute;
    left: 504px;
    top: 420px;
    width: 330px;
    font-size: 13px;
    line-height: 18px;
    white-space: nowrap;
    text-shadow: 0 1px 3px rgba(0,0,0,.35);
  }
  .manifesto p + p { margin-top: 10px; }
  .question {
    position: absolute;
    left: 504px;
    top: 898px;
    font-size: 18px;
    font-weight: 700;
    line-height: 27px;
    white-space: nowrap;
    color: var(--accent-red);
  }
  .search {
    position: absolute;
    left: 504px;
    top: 1000px;
    width: 300px;
    height: 42px;
    display: flex;
    background: var(--field-bg);
  }
  .search-field {
    flex: 1;
    display: flex;
    align-items: center;
    padding-left: 10px;
    font-size: 17px;
    font-weight: 700;
    color: var(--field-ink);
  }
  .search-button {
    width: 72px;
    margin: 4px;
    display: flex;
    align-items: center;
    justify-content: center;
    background: var(--button-bg);
    color: var(--ink-light);
    font-size: 16px;
    font-weight: 700;
  }
  .notice {
    position: absolute;
    left: 504px;
    top: 1056px;
    font-size: 11px;
    color: var(--ink-light);
  }
</style>
</head>
<body>
<main class="poster">
  <div class="sky-photo" role="img" aria-label="曇り空を見上げた写真と、空に向かって伸びる鉄柱"></div>

  <h1 class="headline">スーツを着た仕事が<br>幸せだと<br>思い込んでないか?</h1>

  <section class="manifesto">
    <p>人生にレールなんて無い。<br>あるのは自分と世界との関わりだけ。<br>幸せを規定するのは世界じゃない。<br>自分自身だ。<br>全ての価値観を捨てたとき、<br>未来に何を描けるだろう。</p>
    <p>やりたいことが見つからないなんて当たり前だ。<br>試しに周りの大人に聞いてみたらいい。<br>「やりたいこと、仕事にできてますか?」<br>きっと曖昧な答えしか返ってこない。</p>
    <p>もう認めよう。<br>君は特別じゃない。<br>何者にもなれはしない。<br>環境も選べはしない。<br>自分探しなんてもう十分だ。</p>
    <p>認めよう。<br>全てそこから始まる。</p>
    <p>誰もがみな目的地なんてわかってない。<br>それでも、<br>それでも歩くしかない。</p>
  </section>

  <p class="question">変わり続ける自分は<br>会社に何を期待すればいいんだろう。</p>

  <div class="search">
    <div class="search-field">松浦産業株式会社</div>
    <div class="search-button">検索</div>
  </div>

  <p class="notice">説明会情報は弊社HPでご確認ください</p>
</main>
</body>
</html>
```